KELTO Robotics Engineering Design Team - Pull Up Banner Design

I need a pull-up banner design which I can use at trade shows and events to market our research and development group. We are specialist design engineers who have expertise in:
- Embedded Electronics and Circuit Design
- Rapid Functional Prototyping
- Sensor and Vision Systems
- Robotics Systems

Recent projects include:
- Robotic concrete sewer probes
- IoT wildlife tracking systems
- Robots for exploring wombat burrows
- Smart pest control technology

Target Market(s)

Potential clients who want us to design a project for them

Industry/Entity Type

Engineering Consulting

Colors

Designer to choose colors to be used in the design.

Requirements
Must have
• Look professional and have a high-tech feel to it

```html
<!DOCTYPE html>
<html lang="en">
<head>
<meta charset="utf-8">
<title>KELTO Robotics Engineering Design Team – Pull Up Banner</title>
<link rel="stylesheet" href="https://fonts.googleapis.com/css2?family=Saira:wght@400;800&family=Roboto+Condensed:wght@700&display=swap">
<style>
  :root {
    --page-bg: #eceded;
    --brand-blue: #2f4a9c;
    --brand-red: #c1343c;
    --navy: #0a1a7a;
    --electric: #1f35ff;
    --violet: #5a2bd0;
    --white: #ffffff;
    --field-green: #6f7d48;
    --sky: #9fb8d8;
  }
  html, body {
    margin: 0;
    width: 1200px;
    height: 1200px;
    overflow: hidden;
    background: var(--page-bg);
  }
  .banner {
    position: absolute;
    left: 368px;
    top: 36px;
    width: 464px;
    height: 1126px;
    box-shadow: 0 2px 8px rgba(0,0,0,0.15);
  }
  .wordmark { font-family: "Saira", sans-serif; font-weight: 800; fill: var(--brand-blue); }
  .tagline { font-family: "Saira", sans-serif; font-weight: 400; fill: var(--brand-blue); }
  .panel-text { font-family: "Roboto Condensed", sans-serif; font-weight: 700; fill: var(--white); }
  .web-address { font-family: "Saira", sans-serif; font-weight: 400; fill: var(--white); }
</style>
</head>
<body>
<svg class="banner" viewBox="460 45 580 1407" xmlns="http://www.w3.org/2000/svg">
  <defs>
    <linearGradient id="top-wash" x1="0" y1="0" x2="0" y2="1">
      <stop offset="0" stop-color="#ffffff"/>
      <stop offset="1" stop-color="#f1f4f8"/>
    </linearGradient>
    <linearGradient id="blue-field" x1="0" y1="1" x2="1" y2="0">
      <stop offset="0" stop-color="var(--navy)"/>
      <stop offset="0.6" stop-color="var(--electric)"/>
      <stop offset="1" stop-color="var(--violet)"/>
    </linearGradient>
    <linearGradient id="blue-field-low" x1="0" y1="1" x2="1" y2="0">
      <stop offset="0" stop-color="#1233c8"/>
      <stop offset="0.5" stop-color="#0c1f9a"/>
      <stop offset="1" stop-color="var(--electric)"/>
    </linearGradient>
    <linearGradient id="footer-field" x1="0" y1="0" x2="0" y2="1">
      <stop offset="0" stop-color="#0a1670"/>
      <stop offset="1" stop-color="#1c54d8"/>
    </linearGradient>
    <linearGradient id="site-photo" x1="0" y1="0" x2="0" y2="1">
      <stop offset="0" stop-color="var(--sky)"/>
      <stop offset="0.45" stop-color="#a99a7c"/>
      <stop offset="1" stop-color="var(--field-green)"/>
    </linearGradient>
  </defs>

  <rect class="banner-top" x="460" y="45" width="580" height="1407" fill="url(#top-wash)"/>

  <text class="wordmark" x="750" y="242" text-anchor="middle" font-size="84" letter-spacing="18">KELTO</text>
  <text class="tagline" x="753" y="286" text-anchor="middle" font-size="24">ROBOTICS | AUTOMATION | MECHATRONICS</text>
  <text class="tagline" x="753" y="317" text-anchor="middle" font-size="24" letter-spacing="2">PROTOTYPING | SENSING</text>

  <polygon class="red-wedge" points="460,318 815,443 460,570" fill="var(--brand-red)"/>

  <polygon class="expertise-panel" points="462,597 1040,390 1040,796" fill="url(#blue-field)"/>
  <polygon class="projects-panel" points="460,615 1040,820 1040,842 460,1025" fill="url(#blue-field-low)"/>

  <text class="panel-text" font-size="22">
    <tspan x="718" y="542">Specialist Expertise in:</tspan>
    <tspan x="718" y="566">- Embedded Electronics and</tspan>
    <tspan x="731" y="589">Circuit Design</tspan>
    <tspan x="718" y="613">- Rapid Functional Prototyping</tspan>
    <tspan x="718" y="637">- Sensor and Vision Systems</tspan>
    <tspan x="718" y="661">- Robotics Systems</tspan>
  </text>

  <text class="panel-text" font-size="25">
    <tspan x="487" y="769">Recent Projects include:</tspan>
    <tspan x="487" y="796">- Robotic concrete sewer probes</tspan>
    <tspan x="487" y="823">- IoT wildlife tracking systems</tspan>
    <tspan x="487" y="850">- Robots for exploring wombat burrows</tspan>
    <tspan x="487" y="877">- Smart pest control technology</tspan>
  </text>

  <g role="img" aria-label="Photo of the engineering team in hi-vis gear testing a sewer probe at a manhole on a rural site, with work vehicles behind">
    <polygon points="460,1045 1040,848 1040,1280 460,1280" fill="url(#site-photo)"/>
  </g>

  <rect class="footer-band" x="460" y="1280" width="580" height="172" fill="url(#footer-field)"/>
  <text class="web-address" x="750" y="1359" text-anchor="middle" font-size="44">keltolaboratory.com</text>
</svg>
</body>
</html>
```